Kelvara Learning Australia - Course Brochure Design

Kelvara Learning Australia is a Private Register Training Organisation that delivery accredited training courses to students. These courses are delivery via face to face training and distance education (e.g. elearning).

We are looking to get a template designed via adobe in design that we can use for each of our courses and list the information relevant for each one.

It will need to be around 3 - 4 pages long to be able to fit the information required into the brochure, i have attached some example of other providers course information sheets.

From the examples you'll be able to see that most of the information will remained the same until it gets to the course structure.

I would like it to be kept within our current theme, we are in the middle of upgrading our new website and look (www.kelvara.com.au/drupal).

I look forward to see what you all come back with.
Updates

Project Deadline Extended
Reason: Hi everyone, Thanks for submitting your design, I have extended the deadline due to not many designs have been submitted. I will be review and providing feedback on the designed submitted this week and will provide some more information based off the work and direction of the designs submitted. Thanks, Pedro.

Target Market(s)

our target market is business and individuals who would like to undergo training course. This brochure needs to display the require information.

Industry/Entity Type

Education

Requirements
Must have
• The brochure must have a front page with a design to list our company logo and information and the course title.

A call to action must be on every page, e.g. footer to enrol now call kelvra on 1800 392 058 or visit www.kelvara.com.au

Nice to have
• Some picture to fill the pages would add a nice look

```html
<!DOCTYPE html>
<html lang="en">
<head>
<meta charset="utf-8">
<title>Kelvara Learning Australia – Course Brochure</title>
<link href="https://fonts.googleapis.com/css2?family=Oswald:wght@500;700&family=Open+Sans:ital,wght@0,400;0,600;0,700;1,400&display=swap" rel="stylesheet">
<style>
:root{
  --navy:#2b5a7e;
  --navy-dark:#1f4866;
  --gold:#d9a03c;
  --gold-soft:#e2b15a;
  --cream:#f4e7d2;
  --sky:#e3ecf4;
  --charcoal:#3b3b3b;
  --ink:#222;
  --grey-word:#b9b9b9;
  --white:#fff;
  --red:#8a1c1c;
}
*{box-sizing:border-box;margin:0;padding:0}
html,body{width:1200px;height:900px;overflow:hidden;background:var(--white)}
body{position:relative;font-family:"Open Sans",Arial,sans-serif;color:var(--ink)}
.page{position:absolute;width:330px;height:428px;background:var(--white);box-shadow:0 0 0 1px #ddd;overflow:hidden}
.p1{left:25px;top:10px}.p2{left:435px;top:10px}.p3{left:845px;top:10px}.p4{left:435px;top:457px}
.abs{position:absolute}
.word{position:absolute;font-family:"Oswald",Impact,sans-serif;font-weight:700;text-transform:uppercase;line-height:.9;white-space:nowrap;letter-spacing:-.3px}
.w-gold{color:var(--gold)}.w-grey{color:var(--grey-word)}.w-white{color:#eee}
.small{font-size:4.6px;line-height:1.45}
ul.dash{list-style:none}
ul.dash li::before{content:"- "}
ul.dot{list-style:none}
ul.dot li::before{content:"• "}
.footer{position:absolute;left:0;right:0;bottom:0;height:18px;display:flex;align-items:center}
.footer-cta{flex:0 0 172px;padding-left:14px;font-size:5.4px;font-weight:700;color:var(--navy-dark);border-top:1px solid var(--navy);height:100%;display:flex;align-items:center}
.footer-bar{flex:1;height:100%;background:linear-gradient(90deg,#222,#555 60%,#eee)}
.brand{font-family:"Open Sans",Arial,sans-serif;font-weight:700;color:var(--red);display:flex;align-items:center;gap:4px}
.brand .mark{width:9px;height:9px;background:var(--red)}
</style>
</head>
<body>

<!-- Page 1: cover -->
<section class="page p1">
  <div class="abs" style="left:0;top:0;width:330px;height:125px;background:var(--navy)"></div>
  <p class="abs" style="left:24px;top:52px;width:240px;font-size:13px;line-height:1.15;color:var(--gold-soft)">are you missing out on $4,000 of government training incentives per eligible employee</p>
  <div class="abs" style="left:238px;top:-8px;font-family:'Oswald',sans-serif;font-weight:500;font-size:128px;line-height:1;color:var(--gold)">?</div>

  <div class="abs" style="left:0;top:125px;width:330px;height:145px;background:linear-gradient(180deg,#505050,#2f2f2f)"></div>
  <span class="word w-gold" style="left:50px;top:128px;font-size:24px">Real Estate</span>
  <svg class="abs" style="left:186px;top:130px" width="110" height="20">
    <circle cx="10" cy="10" r="9" fill="#d9a03c"/><circle cx="32" cy="10" r="9" fill="#a36a1c"/>
    <circle cx="54" cy="10" r="9" fill="#2b5a7e"/><circle cx="76" cy="10" r="9" fill="#1d2f44"/><circle cx="98" cy="10" r="9" fill="#6d6d6d"/>
  </svg>
  <span class="word w-gold" style="left:50px;top:153px;font-size:14px;color:#b3781f">Manufacturing</span>
  <span class="word w-white" style="left:50px;top:167px;font-size:24px">Business</span>
  <span class="word w-gold" style="left:156px;top:155px;font-size:44px">Retail</span>
  <span class="word w-grey" style="left:50px;top:192px;font-size:18px">Automotive</span>
  <span class="word w-gold" style="left:158px;top:197px;font-size:11px">Financial Services</span>
  <span class="word w-gold" style="left:50px;top:210px;font-size:38px">Management</span>
  <span class="word w-grey" style="left:50px;top:244px;font-size:26px">Customer Contact</span>

  <p class="abs" style="left:55px;top:272px;width:210px;font-size:5.8px;line-height:1.3;color:var(--navy)">“An organisation’s ability to learn and translate that learning into action is the ultimate competitive advantage”<br><em style="color:var(--ink)">Marcus Hollin, CEO of Norvane Group</em></p>
  <div class="abs" style="left:288px;top:258px;width:26px;height:26px;background:#c9342f;border-radius:2px"></div>

  <div class="abs" role="img" aria-label="Photo of graduates in gowns throwing their caps in the air" style="left:55px;top:305px;width:62px;height:123px;background:linear-gradient(180deg,#d7dde3,#6c7a88 55%,#2b2b2b)"></div>
  <div class="abs" style="left:55px;top:305px;width:8px;height:123px;background:var(--navy)"></div>
  <div class="brand abs" style="left:132px;top:372px;font-size:10px"><span class="mark"></span>Kelvara</div>
  <div class="abs small" style="left:198px;top:375px;width:130px;font-size:4.7px">Kelvara Learning Australia<br>Address - 12/40 Larkmoor St,<br>Orchard Hill, Brisbane, QLD, 4199<br>PO BOX 27, Tallow Bay QLD 4198<br>Email - info@kelvara.com.au<br>Phone - 1800 392 058<br>Fax - 1800 510 274</div>
</section>

<!-- Page 2 -->
<section class="page p2">
  <div class="abs" style="left:0;top:0;width:330px;height:28px;background:var(--navy);color:#fff;font-weight:700;font-size:12px;padding:7px 18px">Are you missing out?</div>
  <div class="abs" style="left:0;top:28px;width:330px;height:16px;background:linear-gradient(90deg,#2b5a7e,#222 70%);color:#fff;font-size:6px;padding:4px 18px">Discover how to have a career/team that is:</div>
  <ul class="dash abs small" style="left:18px;top:62px;font-size:5px;font-weight:600;color:#444">
    <li>continuously improving</li><li>increasing profits</li><li>implementing positive change</li><li>improving efficiencies</li><li>maximising productivity</li>
  </ul>
  <p class="abs small" style="left:132px;top:62px;width:160px;font-size:4.8px;color:#3b79b0">The Government understands the nation’s competitive advantage is based on human capital, so a portion of Government revenue is given back in employer training incentives. This covers up to 100% of nationally accredited training undertaken by your team.</p>
  <div class="abs" style="left:0;top:108px;width:330px;height:18px;background:var(--gold);color:#fff;font-weight:700;font-size:10px;padding:3px 18px">Australian Salescraft Training Co</div>
  <div class="abs" style="left:0;top:126px;width:330px;height:12px;background:linear-gradient(90deg,#777,#222);color:#fff;font-size:5px;padding:3px 18px">MAKES THE</div>
  <ul class="dash abs small" style="left:18px;top:145px;font-size:5px;font-weight:600;color:#444">
    <li>assisting you to source funding</li><li>organising your nationally accredited training courses</li><li>conducting the training/assessments</li><li>driving continuous improvement</li>
  </ul>
  <div class="abs" style="left:0;top:191px;width:330px;height:25px;background:linear-gradient(90deg,#c98a2a,var(--gold-soft) 50%,#c98a2a);text-align:center;font-style:italic;font-size:13px;line-height:25px">don’t blame them … train them!</div>
  <div class="abs" style="left:18px;top:221px;font-size:8.5px;font-weight:700;color:var(--navy-dark)">Getting the most from your people…talent development</div>
  <div class="abs" style="left:0;top:234px;width:330px;height:1px;background:var(--navy)"></div>

  <div class="abs" style="left:0;top:236px;width:165px;height:14px;background:var(--sky);color:var(--navy);font-weight:700;font-size:7px;padding:2px 18px">Simple example</div>
  <div class="abs" style="left:165px;top:236px;width:165px;height:14px;background:var(--cream);color:#555;font-weight:700;font-size:7px;padding:2px 6px">Eligibility and incentives available</div>
  <div class="abs small" style="left:0;top:250px;width:165px;height:124px;background:var(--navy);color:#e8eef3;padding:6px 10px 0 18px;font-size:4.3px">
    <p>There are 30 staff in a business or department.</p><br>
    <p>25 people are eligible for government funding, five are ineligible. The manager / owner identifies all of those people will benefit from training which helps strengthen the organisation. All are existing employees. All 30 participate, funded and unfunded.</p><br>
    <p>The government offers incentives for employers beginning, and again for completing, a nationally recognised training qualification. In this example, the incentivised training is in Frontline Management (Cert IV Frontline Management BSB40807).</p><br>
    <p>All staff complete this training over a period of up to 24 months.</p><br>
    <p>Recognition of Prior Learning is available and encouraged.</p><br>
    <p>The funding received is sufficient to cover both funded and unfunded employees for the training. Everyone participates. Everyone is trained.</p>
  </div>
  <p class="abs small" style="left:18px;top:378px;width:140px;font-size:3.9px;color:#666">Disclaimer: Eligibility of employees to attract incentives depends on whether they meet eligibility requirements of the program. The courses applied for must be of duration of 24 months or more.</p>
  <div class="abs small" style="left:165px;top:250px;width:165px;height:160px;background:var(--gold);padding:5px 8px;font-size:4.3px">
    <p><b>1) Existing worker incentive</b><br>Employed longer than three months full-time or 12 months part-time.<br>Employers are eligible for:<br>Standard Commencement Incentive ($1,500) three months from commencement,<br>plus a Completion Incentive ($2,500), total $4,000</p><br>
    <p><b>2) New worker incentive</b><br>Employed less than three months full-time and 12 months part-time.<br>Employers are eligible for:<br>Standard Commencement Incentive ($1,500) three months from commencement,<br>plus a Completion Incentive ($2,500), total $4,000</p><br>
    <p>Must work an average of 15 hours per week. Must not have a prior tertiary qualification in the same subject area completed in the past seven years.</p><br>
    <p><b>3) Additional incentives</b><br>In many cases there are additional advantages with payroll tax and workers compensation incentives available.<br>There are additional incentives available in skills shortage areas and for mature aged workers.</p>
  </div>
  <div class="footer"><span class="footer-cta">To enrol call 1800 392 058 or visit www.kelvara.com.au</span><span class="footer-bar"></span></div>
</section>

<!-- Page 3 -->
<section class="page p3">
  <div class="abs" style="left:0;top:0;width:330px;height:165px;background:linear-gradient(180deg,#2e3944,#3c3c3c 60%,#4a4a4a)"></div>
  <span class="word w-grey" style="left:18px;top:38px;font-size:40px">Hospitality</span>
  <span class="word w-white" style="left:218px;top:55px;font-size:21px">Floristry</span>
  <span class="word w-gold" style="left:18px;top:78px;font-size:46px">Sales</span>
  <span class="word w-gold" style="left:163px;top:80px;font-size:32px">Tourism</span>
  <span class="word w-grey" style="left:163px;top:111px;font-size:15px">Project Management</span>
  <span class="word" style="left:18px;top:126px;font-size:28px;color:#d06a1a">Warehouse/Logistics</span>

  <div class="abs" style="left:0;top:177px;width:165px;height:14px;background:var(--sky);color:var(--navy);font-weight:700;font-size:7px;padding:2px 18px">Government Accredited Programs</div>
  <div class="abs" style="left:165px;top:177px;width:165px;height:14px;background:var(--cream);color:#555;font-weight:700;font-size:7px;padding:2px 12px">Bonus Resources including</div>
  <ul class="dot abs" style="left:0;top:191px;width:165px;height:146px;background:var(--navy);color:#fff;padding:6px 20px;font-size:5.4px;line-height:1.4">
    <li>Retail</li><li>Business - Sales, Administration</li><li>Frontline Management/Leadership</li><li>Communication</li><li>Transport and Logistics</li><li>Process Manufacturing</li><li>Lean Manufacturing</li><li>Real Estate - Licence Programs</li><li>Automotive</li><li>Floristry</li><li>Hospitality</li><li>Tourism/Travel</li><li>Financial Services</li><li>Project Management</li><li>Aged Care</li>
  </ul>
  <div class="abs small" style="left:0;top:337px;width:165px;height:63px;background:linear-gradient(135deg,#3a3a3a,#1e1e1e);color:#eee;padding:14px 12px 0 18px;font-size:4.9px">
    <p>All our trainers have vast experience in the courses they facilitate.</p>
    <p style="margin-top:3px">They are all accredited with Certificate IV in Workplace Training and Assessment which compliment their various industry specific qualifications.</p>
  </div>
  <ul class="dot abs small" style="left:165px;top:191px;width:165px;height:209px;background:var(--gold);padding:6px 8px 0 12px;font-size:4.2px">
    <li><b>DVD Training Library Membership</b><br>&nbsp;&nbsp;Over 888 titles available in over 20 categories - www.learnreel.com.au</li><br>
    <li><b>eBooks</b><br>&nbsp;&nbsp;An ebook is sent to all candidates monthly over 100 titles www.pagewise.com.au</li><br>
    <li><b>C Ds</b><br>&nbsp;&nbsp;A monthly CD is sent out on a relevant topic to all candidates.</li><br>
    <li><b>Public Programs</b><br>&nbsp;&nbsp;Join us at our public programs saving 50%.</li><br>
    <li><b>T ips, Tactics, Techniques</b><br>&nbsp;&nbsp;Receive our monthly newsletter to promote ongoing improvement.</li><br>
    <li><b>A rticles</b><br>&nbsp;&nbsp;Over 500 articles on our website for free download - many topics.</li><br>
    <li><b>Distance Learning / E Learning</b><br>&nbsp;&nbsp;Most programs can be completed by distance learning or a combination of face to face plus e-learning.</li><br>
    <li><b>Video Streaming</b><br>&nbsp;&nbsp;Our most popular programs available to you wherever you want via website.</li><br>
    <li><b>P lain Lessons</b><br>&nbsp;&nbsp;We are now a distributor for Plain Lessons, a company publishing corporate gift books to reinforce core values.</li>
  </ul>
  <div class="footer"><span class="footer-cta">To enrol call 1800 392 058 or visit www.kelvara.com.au</span><span class="footer-bar"></span></div>
</section>

<!-- Page 4 -->
<section class="page p4">
  <div class="abs" style="left:0;top:0;width:165px;height:26px;background:var(--sky);color:var(--navy);font-weight:700;font-size:8px;padding:8px 22px">Benefits to you</div>
  <div class="abs" style="left:165px;top:0;width:165px;height:26px;background:var(--cream);color:#555;font-weight:700;font-size:8px;padding:8px 32px">Program payment</div>
  <ul class="dot abs" style="left:0;top:26px;width:165px;height:326px;background:var(--navy);color:#fff;padding:10px 12px 0 22px;font-size:5px;line-height:1.4">
    <li>Increasing productivity:<br>&nbsp;&nbsp;People perform better with improved skills.</li><br>
    <li>Tailoring training to suit you:<br>&nbsp;&nbsp;Each onsite course is tailored to your organisation to focus on challenges affecting your team.</li><br>
    <li>Government Accredited Programs:<br>&nbsp;&nbsp;On completion, all candidates receive a nationally recognised award.</li><br>
    <li>Continuously improving:<br>&nbsp;&nbsp;Ongoing regular training promotes a positive work culture rewarding improvement.</li><br>
    <li>Building motivated teams:<br>&nbsp;&nbsp;Onsite training gets your team working on challenges and solutions affecting your organisation. They feel empowered to contribute to positive change.</li><br>
    <li>Saving travel time, disruption and costs:<br>&nbsp;&nbsp;Onsite training is the most cost-effective training option for many organisations.</li><br>
    <li>Enrolling in Best Practice:<br>&nbsp;&nbsp;Training gives the opportunity to standardise systems and processes to “Best Practice”</li><br>
    <li>You’re in good company: Our clients include recognised organisations: Corvell Telecom, Harlow Partners, Bexon Electronics, Marsh + Tolland, Figurecraft Studios, Orient Skyways, Veltro Motors, Toolhaven, Agrowell, Meridian Air, Netcove, Paintwell, Rapid Trade Supplies, QPR, Sentry Guard, Terra Atlas</li>
  </ul>
  <div class="abs small" style="left:165px;top:26px;width:165px;height:40px;background:var(--gold);padding:6px 10px;font-size:5px">Our aim is to provide all these programs for you on a cash neutral basis. Our Business Development Manager will discuss this opportunity with you.</div>
  <div class="abs" style="left:165px;top:66px;width:165px;height:20px;background:linear-gradient(90deg,#ddd,#888);color:#222;font-size:8px;padding:5px 22px">Next Step</div>
  <div class="abs small" style="left:165px;top:86px;width:165px;height:128px;background:linear-gradient(90deg,#2a2a2a,#3a3a3a 70%,#777);color:#eee;padding:6px 10px 0 22px;font-size:4.9px">
    <p>Simply supply us (on our client information form) the full name, date of birth, start date, full/part-time (minimum 15 hours per week), job location (state) and current job title of each of the employees requiring training.</p>
    <p style="margin-top:4px">We then give you an incentive budget.</p>
    <p style="margin-top:4px">Once you have your incentive estimate, we discuss your training needs and agenda, and create a unique web based members page.</p>
    <p style="margin-top:4px">We personalise the program to your needs.</p>
    <p style="margin-top:4px">We meet your employees and set dates.</p>
    <p style="margin-top:4px">We enrol team members.</p>
    <p style="margin-top:4px">We start.</p>
  </div>
  <div class="brand abs" style="left:200px;top:368px;font-size:12px"><span class="mark"></span>Kelvara</div>
  <div class="footer"><span class="footer-cta">To enrol call 1800 392 058 or visit www.kelvara.com.au</span><span class="footer-bar"></span></div>
</section>

</body>
</html>
```